Church Offering Envelope for receive weekly offerings

I need the front of an 6 3/4 envelope designed to be a church offering envelope. Our color palette is CMYK, 1a56b7, e8da7e, 19a3a3, 40c7f1, e7282d.
I need all of the text information carried forward from our old envelope (see attached) but the new style needs to be modern and flat. (Don't want another dove and clouds theme) I need a 1/4 border on all four sides as envelopes cannot be printed full bleed.
Logo is attached
Target Market(s)
Church
Industry/Entity Type
Church
Font styles to use
Sans Serif
Requirements
Must have
- must adhere to the color palette is CMYK, 1a56b7, e8da7e, 19a3a3, 40c7f1, e7282d.
- I need all of the text information carried forward from our old envelope (see attached)

```html
<!DOCTYPE html>
<html lang="en">
<head>
<meta charset="utf-8">
<title>Grace Harbor Ministries – Offering Envelope</title>
<link rel="stylesheet" href="https://fonts.googleapis.com/css2?family=Andika:wght@400;700&display=swap">
<style>
  :root {
    --page-bg: #ffffff;
    --royal: #1a56b7;
    --sand: #e8da7e;
    --sand-light: #f7f0c8;
    --teal: #19a3a3;
    --sky: #40c7f1;
    --sky-light: #c9eefa;
    --red: #e7282d;
    --ink: #14284d;
    --rule: #14284d;
  }
  * { box-sizing: border-box; margin: 0; padding: 0; }
  html, body {
    width: 1200px; height: 638px; overflow: hidden;
    background: var(--page-bg);
    font-family: "Andika", sans-serif;
    color: var(--ink);
  }
  .envelope {
    position: absolute; left: 143px; top: 42px;
    width: 939px; height: 488px; overflow: hidden;
    background: var(--sand-light);
  }
  .envelope__backdrop {
    position: absolute; inset: 0;
    background: linear-gradient(180deg, var(--sky-light) 0%, #e4f4ef 48%, var(--sand-light) 72%, var(--sand) 100%);
  }
  .envelope__band {
    position: absolute; left: 0; right: 0; height: 8px;
  }
  .envelope__band--top { top: 0; background: var(--royal); }
  .envelope__band--teal { bottom: 10px; background: var(--teal); height: 6px; }
  .envelope__band--red { bottom: 0; background: var(--red); height: 10px; }

  .brand {
    position: absolute; left: 50px; top: 108px;
    display: flex; align-items: center; gap: 10px;
  }
  .brand__mark {
    width: 18px; height: 18px; border-radius: 50%;
    background: var(--red);
  }
  .brand__name {
    font-size: 27px; font-weight: 700; color: var(--royal);
    letter-spacing: .5px;
  }
  .verse {
    position: absolute; left: 614px; top: 87px;
    font-size: 16.5px; line-height: 17.6px;
  }
  .field {
    position: absolute; display: flex; align-items: baseline;
    font-size: 20px;
  }
  .field__rule {
    display: inline-block; height: 0;
    border-bottom: 1px dashed var(--rule);
  }
  .field--name { left: 71px; top: 280px; }
  .field--name .field__rule { width: 740px; margin-left: 8px; }
  .field--tithe { left: 71px; top: 346px; }
  .field--tithe .field__rule { width: 170px; margin-left: 3px; }
  .field--radio { left: 411px; top: 346px; }
  .field--radio .field__rule { width: 228px; margin-left: 66px; }
  .checkbox {
    display: inline-block; width: 15px; height: 15px;
    border: 1px solid var(--ink); margin-right: 2px;
    transform: translateY(1px);
  }
  .notice {
    position: absolute; left: 209px; top: 412px;
    font-size: 16.4px; white-space: nowrap;
  }
</style>
</head>
<body>
  <main class="envelope">
    <div class="envelope__backdrop" role="img" aria-label="Soft sky-to-sand backdrop where a light, calm illustration belongs"></div>
    <div class="envelope__band envelope__band--top"></div>
    <div class="envelope__band envelope__band--teal"></div>
    <div class="envelope__band envelope__band--red"></div>

    <div class="brand">
      <span class="brand__mark"></span>
      <span class="brand__name">Grace Harbor Ministries</span>
    </div>

    <p class="verse">“Honour the LORD with thy substance,<br>and with the firstfruits<br>of all thine increase:”;<br>Prov 3:9</p>

    <div class="field field--name"><span>Name:</span><span class="field__rule"></span></div>
    <div class="field field--tithe"><span class="checkbox"></span><span>Tithe/Offering</span><span class="field__rule"></span></div>
    <div class="field field--radio"><span class="checkbox"></span><span>&nbsp;Radio/Webcast</span><span class="field__rule"></span></div>

    <p class="notice">Grace Harbor Ministries does not receive restricted funds in amounts less than $10,000</p>
  </main>
</body>
</html>
```